Professional/modern business card design for construction company

We need a new business card design, double sided keeping it modern, sleek, professional and simple. We are an earthmoving business but do not want any pictures of machinery. I would like one side to have the logo and the other to have all the information, keeping with the colors in our logo. The business card will need to be able to be customised so we can use it for several different managers., we would also like to be able to use the design to apply it to other stationary ie. letterheads, notebooks etc. We do not really have a tag line but we could put on there that we specialise in - Agriculture, Civil Construction and Mining.

Contact Information for Business Card

Brolga Ridge Excavations Pty Ltd
ABN 58 402 937 615
82 Gumleaf Creek Road, Moree NSW 2400

Harold Benton
Managing Director
P 0418 639 204
E haroldbenton@brolgaridgeexc.com.au

Font styles to use
Serif
Sans Serif

Requirements
Nice to have
• I have attached some examples of ideas.
Should not have
• images of machinery

```html
<!DOCTYPE html>
<html lang="en">
<head>
<meta charset="utf-8">
<title>Brolga Ridge Excavations – Business Card</title>
<link rel="stylesheet" href="https://fonts.googleapis.com/css2?family=Lato:wght@400;700;900&family=Michroma&display=swap">
<style>
  :root {
    --canvas: #2b2b2b;
    --card-dark: #474747;
    --card-light: #ffffff;
    --orange: #f28a1e;
    --ink: #3a3a3a;
    --ink-soft: #555555;
    --silver: #d8d8d8;
  }
  * { box-sizing: border-box; margin: 0; padding: 0; }
  html, body { width: 1200px; height: 900px; overflow: hidden; }
  body {
    background: var(--canvas);
    font-family: "Lato", sans-serif;
    position: relative;
  }
  .card {
    position: absolute;
    left: 285px;
    width: 630px;
    height: 360px;
    overflow: hidden;
  }
  /* Front side */
  .card-front {
    top: 55px;
    background: var(--card-dark);
    border-bottom: 7px solid var(--orange);
  }
  .front-brand {
    position: absolute;
    left: 0; right: 0;
    top: 120px;
    text-align: center;
  }
  .front-brand .company {
    font-family: "Lato", sans-serif;
    font-weight: 900;
    font-size: 34px;
    letter-spacing: 1px;
    color: var(--silver);
    text-transform: uppercase;
    line-height: 1.1;
  }
  .front-brand .tagline {
    margin-top: 14px;
    font-size: 17px;
    letter-spacing: 0.8px;
    color: #e4e4e4;
  }
  /* Back side */
  .card-back {
    top: 485px;
    background: var(--card-light);
  }
  .edge-tab {
    position: absolute;
    left: 0;
    top: 118px;
    width: 12px;
    height: 22px;
    background: var(--card-dark);
  }
  .back-brand {
    position: absolute;
    right: 36px;
    top: 52px;
    text-align: right;
    font-weight: 900;
    font-size: 22px;
    line-height: 1.15;
    color: var(--ink);
    text-transform: uppercase;
    letter-spacing: 0.5px;
  }
  .holder {
    position: absolute;
    left: 48px;
    top: 118px;
  }
  .holder .name {
    font-family: "Michroma", sans-serif;
    font-size: 25px;
    font-weight: 400;
    color: var(--orange);
    letter-spacing: 1px;
    -webkit-text-stroke: 0.8px var(--orange);
  }
  .holder .role {
    margin-top: 4px;
    font-size: 17px;
    letter-spacing: 1px;
    color: var(--ink-soft);
  }
  .divider {
    position: absolute;
    left: 232px;
    right: 36px;
    top: 176px;
    height: 2px;
    background: var(--ink);
  }
  .contact-list {
    position: absolute;
    left: 48px;
    top: 196px;
    list-style: none;
  }
  .contact-list li {
    display: flex;
    align-items: center;
    gap: 12px;
    font-size: 17px;
    letter-spacing: 0.6px;
    color: var(--ink);
    height: 30px;
  }
  .contact-list svg { width: 16px; height: 16px; flex: none; }
  .company-details {
    position: absolute;
    right: 36px;
    top: 222px;
    text-align: right;
    font-size: 18px;
    letter-spacing: 0.8px;
    line-height: 1.45;
    color: var(--ink);
  }
  .company-details .label { color: var(--orange); }
</style>
</head>
<body>

<section class="card card-front" aria-label="Business card front">
  <div class="front-brand">
    <p class="company">Brolga Ridge<br>Excavations Pty Ltd</p>
    <p class="tagline">Agriculture, Civil Construction and Mining</p>
  </div>
</section>

<section class="card card-back" aria-label="Business card back">
  <div class="edge-tab"></div>
  <p class="back-brand">Brolga Ridge<br>Excavations Pty Ltd</p>

  <div class="holder">
    <p class="name">HAROLD BENTON</p>
    <p class="role">Managing Director</p>
  </div>
  <div class="divider"></div>

  <ul class="contact-list">
    <li>
      <svg viewBox="0 0 16 16" aria-hidden="true"><rect x="4" y="1" width="8" height="14" rx="1.5" fill="none" stroke="#f28a1e" stroke-width="1.6"/><circle cx="8" cy="12.3" r="0.9" fill="#f28a1e"/></svg>
      0418 639 204
    </li>
    <li>
      <svg viewBox="0 0 16 16" aria-hidden="true"><rect x="1" y="3" width="14" height="10" rx="1" fill="#f28a1e"/><path d="M1.5 3.8 8 9 14.5 3.8" fill="none" stroke="#fff" stroke-width="1.3"/></svg>
      haroldbenton@brolgaridgeexc.com.au
    </li>
    <li>
      <svg viewBox="0 0 16 16" aria-hidden="true"><g fill="none" stroke="#f28a1e" stroke-width="1.3"><circle cx="8" cy="8" r="6.5"/><ellipse cx="8" cy="8" rx="3" ry="6.5"/><path d="M1.5 8h13M2.5 4.8h11M2.5 11.2h11"/></g></svg>
      www.brolgaridgeexc.com.au
    </li>
  </ul>

  <div class="company-details">
    <p><span class="label">ABN</span> 58 402 937 615</p>
    <p>82 Gumleaf Creek Road</p>
    <p>Moree NSW 2400</p>
  </div>
</section>

</body>
</html>
```